Business Card for Marco Thieblin Analytics and Marco Thieblin Photography

I want a double sided business card: on one side it should be about "Marco Thieblin Photography" and on the other side about "Marco Thieblin Analytics". You find the logos for these two projects in the attachments. The design of the business card should blend well with the colours and fonts used in the logos and should be quite simple, yet look professional and modern.

In addition to my name, there should be content for a telephone number, e-mail address and website. There should be little icons (for telephone, email and web) before these fields. I do not want a postal mail address field.
Lastly you should indicate that people can contact me in the following languages: Lëtzebuergesch, Deutsch, Français, English, Castellano, Ido
This should be very unobtrusive: either in a small muted font or with little icons (preferably without using flags as flags represent nations, not languages - one possibility would be by using the 2 letter ISO codes).

The design should be delivered in Adobe Illustrator format or something similar that I can edit easily, as it's possible that I will change my e-mail address and domain soon.

I hope this was detailed enough but still leaves you some freedom for designing something nice.

Thank you!
Marco

Industry/Entity Type

Business

Contact Information for Business Card

e-mail address: mtb_@orvenmail.example
website: www.marcothieblin.example (for Marco Thieblin Photography)
website: kelvodata.example/mtb (for Marco Thieblin Analytics - this address is likely to change)
phone: +352 691 987 654 (not my real number - I prefer not to publish it on the web)

Requirements
Nice to have
• A speech bubble followed by the 2-letter language codes (lb, de, fr, en, es, io) or even speech bubble icons for every language would be nice and eliminates the need to put text like 'you can contact me in the following languages'.

```html
<!DOCTYPE html>
<html lang="en">
<head>
<meta charset="utf-8">
<title>Marco Thieblin – Business Cards</title>
<link rel="stylesheet" href="https://fonts.googleapis.com/css2?family=Libre+Baskerville&family=Roboto+Condensed:wght@300;400&display=swap">
<style>
  :root{
    --bg:#86d9c8;
    --paper:#f3f3f2;
    --ink:#060708;
    --blue:#1ea3e3;
    --blue-deep:#0b5f7e;
    --green:#00a34f;
    --green-light:#7ccd3c;
    --green-deep:#1f6e2a;
    --orange:#ef8a1e;
    --muted:#6a6a6a;
    --dark-text:#4a4a4a;
    --light-text:#f2f2f2;
  }
  *{box-sizing:border-box;margin:0;padding:0}
  html,body{width:1154px;height:1200px;overflow:hidden}
  body{background:var(--bg);font-family:"Roboto Condensed",sans-serif;position:relative}

  .card{position:absolute;left:267px;width:620px;height:380px;background:var(--paper);overflow:hidden;box-shadow:0 18px 30px rgba(0,60,50,.25)}
  .card--photo{top:150px}
  .card--analytics{top:670px}

  .panel-dark{position:absolute;background:var(--ink)}
  .name-band{position:absolute;display:flex;align-items:center;color:#fff;white-space:nowrap;
    font-family:"Libre Baskerville",serif;letter-spacing:1px;text-transform:uppercase}
  .fold{position:absolute}

  .brand{position:absolute;display:flex;align-items:center;gap:10px;white-space:nowrap;
    font-family:"Roboto Condensed",sans-serif;font-weight:400;font-size:20px;color:var(--orange)}
  .brand__dot{width:14px;height:14px;border-radius:50%;background:var(--orange);flex:none}

  .contacts{position:absolute;list-style:none;font-weight:300;font-size:18px;white-space:nowrap}
  .contacts li{display:flex;align-items:center;gap:14px;height:38px}
  .contacts svg{width:22px;height:22px;flex:none}

  .languages{position:absolute;display:flex;align-items:center;gap:4px;font-weight:300;white-space:nowrap}
  .languages__label{font-size:13px;margin-right:6px}
  .bubble{width:24px;height:26px;flex:none}

  /* photography side */
  .card--photo .panel-dark{left:0;top:40px;width:330px;height:340px}
  .card--photo .name-band{left:230px;top:40px;width:390px;height:64px;padding-left:34px;font-size:30px;background:var(--blue)}
  .card--photo .fold{left:300px;top:104px;width:34px;height:276px;background:linear-gradient(90deg,var(--blue-deep),#1586b4)}
  .card--photo .paper-panel{position:absolute;left:334px;top:104px;width:286px;height:276px;background:var(--paper)}
  .card--photo .brand{left:26px;top:210px}
  .card--photo .contacts{left:354px;top:124px;color:var(--dark-text)}
  .card--photo .contacts svg{stroke:var(--blue)}
  .card--photo .languages{left:354px;top:320px;color:var(--muted)}

  /* analytics side */
  .card--analytics .panel-dark{left:300px;top:40px;width:320px;height:340px}
  .card--analytics .name-band{left:330px;top:40px;width:290px;height:64px;padding-left:18px;font-size:23px;background:var(--green)}
  .card--analytics .fold{left:296px;top:40px;width:36px;height:340px;background:linear-gradient(180deg,var(--green-light),var(--green-deep))}
  .card--analytics .brand{left:36px;top:170px}
  .card--analytics .contacts{left:354px;top:124px;color:var(--light-text)}
  .card--analytics .contacts svg{stroke:var(--green)}
  .card--analytics .languages{left:354px;top:320px;color:var(--light-text)}
</style>
</head>
<body>

<section class="card card--photo" aria-label="Photography side">
  <div class="panel-dark"></div>
  <div class="fold"></div>
  <div class="paper-panel"></div>
  <div class="name-band">Marco Thieblin</div>
  <div class="brand"><span class="brand__dot"></span>Marco Thieblin Photography</div>
  <ul class="contacts">
    <li><svg viewBox="0 0 24 24" fill="none" stroke-width="1.5"><rect x="2" y="5" width="20" height="14"/><path d="M2 5l10 8 10-8M2 19l8-7M22 19l-8-7"/></svg>mtb_@orvenmail.example</li>
    <li><svg viewBox="0 0 24 24" fill="none" stroke-width="1.5"><circle cx="12" cy="12" r="10"/><ellipse cx="12" cy="12" rx="4.5" ry="10"/><path d="M2 12h20M4 7h16M4 17h16"/></svg>www.marcothieblin.example</li>
    <li><svg viewBox="0 0 24 24" fill="none" stroke-width="1.5"><rect x="6" y="2" width="12" height="20" rx="2"/><path d="M10 19h4"/></svg>+352 691 987 654</li>
  </ul>
  <div class="languages">
    <span class="languages__label">Contact me in:</span>
    <svg class="bubble" viewBox="0 0 28 30"><path d="M14 2a12 12 0 1 0 5 22.9L24 28l-1.5-6A12 12 0 0 0 14 2z" fill="none" stroke="var(--orange)" stroke-width="1.6"/><text x="14" y="18" text-anchor="middle" font-size="11" fill="var(--orange)" font-family="Roboto Condensed">lb</text></svg>
    <svg class="bubble" viewBox="0 0 28 30"><path d="M14 2a12 12 0 1 0 5 22.9L24 28l-1.5-6A12 12 0 0 0 14 2z" fill="none" stroke="var(--orange)" stroke-width="1.6"/><text x="14" y="18" text-anchor="middle" font-size="11" fill="var(--orange)" font-family="Roboto Condensed">de</text></svg>
    <svg class="bubble" viewBox="0 0 28 30"><path d="M14 2a12 12 0 1 0 5 22.9L24 28l-1.5-6A12 12 0 0 0 14 2z" fill="none" stroke="var(--orange)" stroke-width="1.6"/><text x="14" y="18" text-anchor="middle" font-size="11" fill="var(--orange)" font-family="Roboto Condensed">fr</text></svg>
    <svg class="bubble" viewBox="0 0 28 30"><path d="M14 2a12 12 0 1 0 5 22.9L24 28l-1.5-6A12 12 0 0 0 14 2z" fill="none" stroke="var(--orange)" stroke-width="1.6"/><text x="14" y="18" text-anchor="middle" font-size="11" fill="var(--orange)" font-family="Roboto Condensed">en</text></svg>
    <svg class="bubble" viewBox="0 0 28 30"><path d="M14 2a12 12 0 1 0 5 22.9L24 28l-1.5-6A12 12 0 0 0 14 2z" fill="none" stroke="var(--orange)" stroke-width="1.6"/><text x="14" y="18" text-anchor="middle" font-size="11" fill="var(--orange)" font-family="Roboto Condensed">es</text></svg>
    <svg class="bubble" viewBox="0 0 28 30"><path d="M14 2a12 12 0 1 0 5 22.9L24 28l-1.5-6A12 12 0 0 0 14 2z" fill="none" stroke="var(--orange)" stroke-width="1.6"/><text x="14" y="18" text-anchor="middle" font-size="11" fill="var(--orange)" font-family="Roboto Condensed">io</text></svg>
  </div>
</section>

<section class="card card--analytics" aria-label="Analytics side">
  <div class="fold"></div>
  <div class="panel-dark"></div>
  <div class="name-band">Marco Thieblin</div>
  <div class="brand"><span class="brand__dot"></span>Marco Thieblin Analytics</div>
  <ul class="contacts">
    <li><svg viewBox="0 0 24 24" fill="none" stroke-width="1.5"><rect x="2" y="5" width="20" height="14"/><path d="M2 5l10 8 10-8M2 19l8-7M22 19l-8-7"/></svg>mtb_@orvenmail.example</li>
    <li><svg viewBox="0 0 24 24" fill="none" stroke-width="1.5"><circle cx="12" cy="12" r="10"/><ellipse cx="12" cy="12" rx="4.5" ry="10"/><path d="M2 12h20M4 7h16M4 17h16"/></svg>kelvodata.example/mtb</li>
    <li><svg viewBox="0 0 24 24" fill="none" stroke-width="1.5"><rect x="6" y="2" width="12" height="20" rx="2"/><path d="M10 19h4"/></svg>+352 691 987 654</li>
  </ul>
  <div class="languages">
    <span class="languages__label">Contact me in:</span>
    <svg class="bubble" viewBox="0 0 28 30"><path d="M14 2a12 12 0 1 0 5 22.9L24 28l-1.5-6A12 12 0 0 0 14 2z" fill="none" stroke="var(--orange)" stroke-width="1.6"/><text x="14" y="18" text-anchor="middle" font-size="11" fill="var(--orange)" font-family="Roboto Condensed">lb</text></svg>
    <svg class="bubble" viewBox="0 0 28 30"><path d="M14 2a12 12 0 1 0 5 22.9L24 28l-1.5-6A12 12 0 0 0 14 2z" fill="none" stroke="var(--orange)" stroke-width="1.6"/><text x="14" y="18" text-anchor="middle" font-size="11" fill="var(--orange)" font-family="Roboto Condensed">de</text></svg>
    <svg class="bubble" viewBox="0 0 28 30"><path d="M14 2a12 12 0 1 0 5 22.9L24 28l-1.5-6A12 12 0 0 0 14 2z" fill="none" stroke="var(--orange)" stroke-width="1.6"/><text x="14" y="18" text-anchor="middle" font-size="11" fill="var(--orange)" font-family="Roboto Condensed">fr</text></svg>
    <svg class="bubble" viewBox="0 0 28 30"><path d="M14 2a12 12 0 1 0 5 22.9L24 28l-1.5-6A12 12 0 0 0 14 2z" fill="none" stroke="var(--orange)" stroke-width="1.6"/><text x="14" y="18" text-anchor="middle" font-size="11" fill="var(--orange)" font-family="Roboto Condensed">en</text></svg>
    <svg class="bubble" viewBox="0 0 28 30"><path d="M14 2a12 12 0 1 0 5 22.9L24 28l-1.5-6A12 12 0 0 0 14 2z" fill="none" stroke="var(--orange)" stroke-width="1.6"/><text x="14" y="18" text-anchor="middle" font-size="11" fill="var(--orange)" font-family="Roboto Condensed">es</text></svg>
    <svg class="bubble" viewBox="0 0 28 30"><path d="M14 2a12 12 0 1 0 5 22.9L24 28l-1.5-6A12 12 0 0 0 14 2z" fill="none" stroke="var(--orange)" stroke-width="1.6"/><text x="14" y="18" text-anchor="middle" font-size="11" fill="var(--orange)" font-family="Roboto Condensed">io</text></svg>
  </div>
</section>

</body>
</html>
```